Sliding banner

I need three sliding banners designed for my website korvalent.co.za - please take a look at the existing banner format.

The products items on the banner can be any product that is on the website - the size of the banner must remain the same - the design project is only for the sliding banner.

Regards

```html
<!DOCTYPE html>
<html lang="en">
<head>
<meta charset="utf-8">
<title>USB Dual Car Charger</title>
<link rel="stylesheet" href="https://fonts.googleapis.com/css2?family=Open+Sans:wght@300;400;800&display=swap">
<style>
  :root {
    --bg-light: #f4f4f5;
    --bg-mid: #e6e7e9;
    --facet: #ffffff;
    --ink: #111111;
    --ink-soft: #2b2b2b;
    --accent-blue: #3b9ad8;
    --bar-edge: #d9dadc;
    --white: #ffffff;
    --product-light: #fbfbfb;
    --product-shade: #d7d8da;
  }
  * { box-sizing: border-box; margin: 0; padding: 0; }
  html, body { width: 1200px; height: 406px; overflow: hidden; background: var(--white); }
  .banner {
    position: relative;
    width: 1200px;
    height: 406px;
    overflow: hidden;
    background: radial-gradient(ellipse at 30% 45%, var(--bg-light) 0%, var(--bg-mid) 100%);
    font-family: "Open Sans", Arial, sans-serif;
  }
  .banner__facets { position: absolute; inset: 0; width: 1200px; height: 406px; }
  .banner__copy { position: absolute; left: 72px; top: 52px; width: 620px; }
  .banner__title {
    font-weight: 800;
    font-size: 29px;
    line-height: 34px;
    letter-spacing: 0.6px;
    color: var(--ink);
    text-transform: uppercase;
    white-space: nowrap;
  }
  .banner__text {
    margin-top: 0;
    font-weight: 300;
    font-size: 31px;
    line-height: 38px;
    color: var(--ink-soft);
    white-space: nowrap;
  }
  .product-frame {
    position: absolute;
    left: 755px;
    top: 19px;
    width: 280px;
    height: 280px;
    border-radius: 50%;
    background: var(--white);
    box-shadow: 0 2px 10px rgba(0,0,0,0.06);
  }
  .product-photo {
    position: absolute;
    left: 50px;
    top: 50px;
    width: 185px;
    height: 205px;
    border-radius: 22px;
    background: linear-gradient(160deg, var(--product-light) 0%, var(--product-shade) 100%);
  }
  .caption-bar {
    position: absolute;
    left: 0;
    top: 349px;
    width: 1200px;
    height: 57px;
    background: var(--accent-blue);
    border-top: 2px solid var(--bar-edge);
  }
  .caption-bar__label {
    position: absolute;
    left: 802px;
    top: 13px;
    font-weight: 400;
    font-size: 23px;
    line-height: 28px;
    color: var(--white);
    white-space: nowrap;
  }
</style>
</head>
<body>
  <section class="banner">
    <svg class="banner__facets" viewBox="0 0 1200 406" aria-hidden="true">
      <polygon points="0,0 420,0 160,406 0,406" fill="var(--facet)" opacity="0.35"/>
      <polygon points="300,0 760,0 520,406 120,406" fill="var(--facet)" opacity="0.22"/>
      <polygon points="560,406 1200,120 1200,406" fill="var(--facet)" opacity="0.3"/>
      <polygon points="900,0 1200,0 1200,90" fill="var(--facet)" opacity="0.25"/>
    </svg>

    <div class="banner__copy">
      <h1 class="banner__title">Car Charger Dual USB</h1>
      <p class="banner__text">This clever design gives you 2.1mA<br>on the top USB port and 1mA on the<br>bottom USB port</p>
    </div>

    <div class="product-frame">
      <div class="product-photo" role="img" aria-label="White and black dual USB car charger with a 3.1 amp badge"></div>
    </div>

    <div class="caption-bar">
      <span class="caption-bar__label">USB Dual Car Charger</span>
    </div>
  </section>
</body>
</html>
```